Business Card Lionel/Marta

We would like you to design a business card with the same graphics as the rack card, which is attached, along with our logo. We are looking for a business card for our company director Lionel Parfitt and for myself (Marta de Wintersloot, General Manager).

Reason: We did not provide all relevant information before the end of the original deadline. The brief has now been updated and the deadline extended.

Industry/Entity Type

Business

Requirements
Must have
• We need the logo and the following contact details:

Lionel Parfitt
Company Director
17 Brindle Lane
Mangere, Auckland, 2022
E: lionel@harbourlink4.co.nz
W: www.harbourlink4.co.nz
P: +64 (0)9 4831907
F: +64 (0)9 4831905
M: +64 (0)21 618447
FREE: 0508 391460 (NZ only)

Marta de Wintersloot
General Manager
17 Brindle Lane
Mangere, Auckland, 2022
E: marta@harbourlink4.co.nz
W: www.harbourlink4.co.nz
P: +64 (0)9 4831907
F: +64 (0)9 4831905
M: +64 (0)21 618448

The phrase "Service Excellence".
Nice to have
• We would like to incorporate icons to indicate "phone", "website", "mobile" etc.

```html
<!DOCTYPE html>
<html lang="en">
<head>
<meta charset="utf-8">
<title>Harbourlink 4 Rental Cars – Business Card</title>
<link href="https://fonts.googleapis.com/css2?family=Saira:wght@400;600;800&display=swap" rel="stylesheet">
<style>
  :root {
    --stage: #2a2a2a;
    --card-light: #f4f4f4;
    --card-shade: #d9d9d9;
    --brand-blue: #1f3f9c;
    --brand-red: #e8253f;
    --ink: #333333;
    --icon: #555555;
    --white: #ffffff;
  }
  * { margin: 0; padding: 0; box-sizing: border-box; }
  html, body {
    width: 1200px;
    height: 870px;
    overflow: hidden;
    background: var(--stage);
    font-family: "Saira", sans-serif;
  }
  .stage {
    width: 1200px;
    height: 870px;
    display: flex;
    flex-direction: column;
    align-items: center;
    justify-content: center;
    gap: 30px;
  }
  .card {
    position: relative;
    width: 680px;
    height: 388px;
    overflow: hidden;
    background: linear-gradient(135deg, var(--card-light) 0%, var(--white) 40%, var(--card-shade) 100%);
  }

  /* Back face */
  .card--back {
    display: flex;
    align-items: center;
    justify-content: center;
  }

  /* Brand name block */
  .brand {
    display: flex;
    align-items: center;
    gap: 12px;
    color: var(--brand-blue);
    font-weight: 800;
    line-height: 1;
  }
  .brand__mark {
    width: 22px;
    height: 22px;
    border-radius: 50%;
    background: var(--brand-red);
    flex: none;
  }
  .brand__name {
    display: flex;
    flex-direction: column;
    text-transform: uppercase;
  }
  .brand--large .brand__name { font-size: 40px; letter-spacing: 1px; }
  .brand--large .brand__name small { font-size: 22px; letter-spacing: 3px; margin-top: 6px; }
  .brand--small .brand__name { font-size: 27px; letter-spacing: 1px; }
  .brand--small .brand__name small { font-size: 16px; letter-spacing: 2px; margin-top: 4px; }
  .brand--small .brand__mark { width: 16px; height: 16px; }

  /* Front face */
  .contact-list {
    position: absolute;
    top: 26px;
    left: 34px;
    list-style: none;
    font-size: 13px;
    color: var(--ink);
  }
  .contact-list li {
    display: flex;
    align-items: center;
    gap: 10px;
    height: 22px;
    white-space: nowrap;
  }
  .contact-list svg {
    width: 13px;
    height: 13px;
    fill: var(--icon);
    flex: none;
  }
  .front-brand {
    position: absolute;
    top: 62px;
    right: 34px;
    display: flex;
    flex-direction: column;
    align-items: flex-end;
    gap: 10px;
  }
  .tagline {
    font-size: 14px;
    font-weight: 600;
    letter-spacing: 1px;
    color: var(--brand-red);
  }
  .info-band {
    position: absolute;
    left: 0;
    bottom: 0;
    width: 100%;
    height: 162px;
    background: var(--brand-blue);
    color: var(--white);
  }
  .address {
    position: absolute;
    left: 34px;
    top: 22px;
    font-size: 16px;
    line-height: 1.35;
    letter-spacing: 0.5px;
    font-style: normal;
  }
  .holder {
    position: absolute;
    right: 34px;
    bottom: 30px;
    text-align: right;
  }
  .holder__name {
    font-size: 19px;
    font-weight: 400;
    letter-spacing: 1px;
    text-transform: uppercase;
  }
  .holder__role {
    font-size: 14px;
    letter-spacing: 0.5px;
  }
</style>
</head>
<body>
<main class="stage">

  <section class="card card--back" aria-label="Business card back">
    <div class="brand brand--large">
      <span class="brand__mark"></span>
      <span class="brand__name">Harbourlink 4<small>Rental Cars</small></span>
    </div>
  </section>

  <section class="card card--front" aria-label="Business card front">
    <ul class="contact-list">
      <li>
        <svg viewBox="0 0 16 16"><path d="M3.5 1l3 3-1.6 2a9 9 0 0 0 5.1 5.1l2-1.6 3 3-1.8 2.2C7 14 2 9 1.3 2.8z"/></svg>
        +64 (0)9 4831907
      </li>
      <li>
        <svg viewBox="0 0 16 16"><path d="M4 0h8a1 1 0 0 1 1 1v14a1 1 0 0 1-1 1H4a1 1 0 0 1-1-1V1a1 1 0 0 1 1-1zm1 2v10h6V2zm3 11a1 1 0 1 0 0 2 1 1 0 0 0 0-2z"/></svg>
        +64 (0)21 618447
      </li>
      <li>
        <svg viewBox="0 0 16 16"><path d="M4 0h7l2 2v4h1a2 2 0 0 1 2 2v6h-3v2H3v-2H0V8a2 2 0 0 1 2-2h2zm1 1v5h7V2.5L10.5 1zM4 11v4h8v-4z"/></svg>
        +64 (0)9 4831905
      </li>
      <li>
        <svg viewBox="0 0 16 16"><path d="M3.5 1l3 3-1.6 2a9 9 0 0 0 5.1 5.1l2-1.6 3 3-1.8 2.2C7 14 2 9 1.3 2.8z"/></svg>
        FREE: 0508 391460 (NZ only)
      </li>
      <li>
        <svg viewBox="0 0 16 16"><path d="M0 3h16v10H0zm1.5 1.2L8 9l6.5-4.8V4h-13z"/></svg>
        lionel@harbourlink4.co.nz
      </li>
      <li>
        <svg viewBox="0 0 16 16"><path d="M8 0a8 8 0 1 0 0 16A8 8 0 0 0 8 0zm5.9 7h-2.9a12 12 0 0 0-1.3-5.3A6 6 0 0 1 13.9 7zM8 2a10 10 0 0 1 1.5 5h-3A10 10 0 0 1 8 2zM6.3 1.7A12 12 0 0 0 5 7H2.1a6 6 0 0 1 4.2-5.3zM2.1 9H5a12 12 0 0 0 1.3 5.3A6 6 0 0 1 2.1 9zM8 14a10 10 0 0 1-1.5-5h3A10 10 0 0 1 8 14zm1.7.3A12 12 0 0 0 11 9h2.9a6 6 0 0 1-4.2 5.3z"/></svg>
        www.harbourlink4.co.nz
      </li>
    </ul>

    <div class="front-brand">
      <div class="brand brand--small">
        <span class="brand__mark"></span>
        <span class="brand__name">Harbourlink 4<small>Rental Cars</small></span>
      </div>
      <p class="tagline">Service Excellence</p>
    </div>

    <div class="info-band">
      <address class="address">17 Brindle Lane<br>Mangere, Auckland, 2022</address>
      <div class="holder">
        <p class="holder__name">Lionel Parfitt</p>
        <p class="holder__role">Company Director</p>
      </div>
    </div>
  </section>

</main>
</body>
</html>
```